Baseball Trainer Poster

Looking to put up a poster inside an indoor baseball facility which markets the cost of instruction, but also the trainers who can be hired.
I have done a crude job of building a Power Point which includes the pictures and general details. I was hoping you could crop the pictures of the coaches as needed.
I have also attached our logo.
I have also attached a generic flier we had made for a camp previously.
Name of Indoor Facility is "Slate Harbor"
Just FYI: website is www.SlateHarborFit.example
The ideal colors for the poster are Blue, Red, White & Grey
Look and feel
Each slider illustrates characteristics of the customer's brand and the style your logo design should communicate.

```html
<!DOCTYPE html>
<html lang="en">
<head>
<meta charset="utf-8">
<title>Slate Harbor – Personal Instruction</title>
<link href="https://fonts.googleapis.com/css2?family=Bungee&family=Poppins:wght@400;500;600;700&display=swap" rel="stylesheet">
<style>
  :root{
    --red:#e8141b;
    --navy:#0c2a63;
    --blue:#1b4fa3;
    --bright-blue:#2a6fe0;
    --ink:#14265a;
    --white:#ffffff;
    --grey:#eeeff1;
    --stage:#d7d8da;
    --photo-a:#8a6f5c;
    --photo-b:#3b3f4a;
  }
  *{box-sizing:border-box;margin:0;padding:0}
  html,body{width:1200px;height:2380px;overflow:hidden}
  body{background:var(--stage);font-family:"Poppins",sans-serif;position:relative}
  .poster{position:absolute;left:50px;top:413px;width:1100px;height:1554px;background:var(--white);overflow:hidden;box-shadow:0 10px 30px rgba(0,0,0,.18)}
  .stitch-band{position:absolute;left:0;top:12px;width:100%;height:14px;background:var(--red)}
  .brand{position:absolute;left:60px;top:100px;display:flex;align-items:center;gap:14px}
  .brand-dot{width:34px;height:34px;border-radius:50%;background:var(--navy)}
  .brand-name{font-family:"Poppins",sans-serif;font-weight:700;font-size:36px;color:var(--navy)}
  .pricing{position:absolute;left:542px;top:64px;width:520px}
  .pricing h1{font-family:"Bungee",sans-serif;font-weight:400;color:var(--red);font-size:32px;letter-spacing:0;line-height:1;white-space:nowrap}
  .price-list{list-style:none;margin-top:20px}
  .price-list li{display:flex;align-items:center;gap:14px;font-weight:700;color:var(--ink);font-size:25px;height:49px;white-space:nowrap}
  .price-list svg{flex:none}
  .blue-section{position:absolute;left:0;top:288px;width:100%;height:692px;background:linear-gradient(100deg,var(--blue) 0%,var(--navy) 45%,var(--blue) 100%)}
  .blue-section svg.stripes,.lesson-section svg.stripes{position:absolute;inset:0}
  .banner{position:absolute;left:50%;transform:translateX(-50%);background:var(--red);color:var(--white);font-family:"Bungee",sans-serif;text-align:center;white-space:nowrap;clip-path:polygon(4% 0,100% 0,96% 100%,0 100%)}
  .banner-private{top:258px;width:510px;height:62px;font-size:34px;line-height:62px}
  .banner-lessons{top:935px;width:280px;height:60px;font-size:34px;line-height:60px}
  .seam{position:absolute;top:962px;height:6px;background:var(--red)}
  .seam-left{left:0;width:410px}
  .seam-right{right:0;width:410px}
  .lesson-section{position:absolute;left:0;top:995px;width:100%;height:559px;background:linear-gradient(110deg,#f6f6f7,var(--grey))}
  .coach{position:absolute;width:280px;text-align:center;transform:translateX(-50%)}
  .photo{margin:0 auto;border-radius:50%;background:radial-gradient(circle at 50% 40%,var(--photo-a),var(--photo-b))}
  .trainer .photo{width:180px;height:180px;border:4px solid var(--white)}
  .lesson .photo{width:134px;height:134px}
  .coach-name{color:var(--red);font-weight:700;line-height:1.2}
  .trainer .coach-name{font-size:19px;margin-top:16px}
  .lesson .coach-name{font-size:19px;margin-top:14px}
  .coach-role{font-size:14.5px;line-height:1.4;font-weight:500}
  .trainer .coach-role{color:var(--white)}
  .lesson .coach-role{color:var(--ink)}
  .coach-role.large{font-size:19px;font-weight:400}
  .footer{position:absolute;left:0;top:1512px;width:100%;display:flex;align-items:center;gap:16px}
  .footer .rule{flex:1;height:2px;background:var(--navy)}
  .footer .url{font-size:17px;letter-spacing:4px;color:var(--navy);font-weight:500}
  .footer .url b{color:var(--red);font-weight:700}
</style>
</head>
<body>
<main class="poster">
  <div class="stitch-band"></div>

  <div class="brand">
    <span class="brand-dot"></span>
    <span class="brand-name">Slate Harbor</span>
  </div>

  <section class="pricing">
    <h1>Personal Instruction</h1>
    <ul class="price-list">
      <li><svg width="18" height="18" viewBox="0 0 18 18"><circle cx="9" cy="9" r="9" fill="#e8141b"/><path d="M5 9.3l2.6 2.5L13 6.4" stroke="#fff" stroke-width="2.2" fill="none"/></svg>$35 for tandem lesson (2:1)/Half-HR</li>
      <li><svg width="18" height="18" viewBox="0 0 18 18"><circle cx="9" cy="9" r="9" fill="#e8141b"/><path d="M5 9.3l2.6 2.5L13 6.4" stroke="#fff" stroke-width="2.2" fill="none"/></svg>$50 for private lesson/Half-HR</li>
      <li><svg width="18" height="18" viewBox="0 0 18 18"><circle cx="9" cy="9" r="9" fill="#e8141b"/><path d="M5 9.3l2.6 2.5L13 6.4" stroke="#fff" stroke-width="2.2" fill="none"/></svg>$150 to train 4+ players/1-Hour</li>
    </ul>
  </section>

  <section class="blue-section">
    <svg class="stripes" width="1100" height="692" viewBox="0 0 1100 692" aria-hidden="true">
      <polygon points="0,0 110,0 0,360" fill="#e8141b"/>
      <polygon points="110,0 140,0 0,470 0,410" fill="#2a6fe0"/>
      <polygon points="320,0 520,0 230,692 40,692" fill="#123a82" opacity=".6"/>
      <polygon points="760,0 840,0 560,692 480,692" fill="#2a6fe0" opacity=".35"/>
      <polygon points="1100,340 1100,692 980,692" fill="#e8141b"/>
      <polygon points="1100,250 1100,300 955,692 925,692" fill="#2a6fe0"/>
    </svg>
    <div class="coach trainer" style="left:207px;top:58px">
      <div class="photo" role="img" aria-label="Headshot of trainer Devon Ashcroft"></div>
      <p class="coach-name">Devon Ashcroft</p>
      <p class="coach-role">FormerPro Pitcher Minors<br>(Lancers &amp; Comets</p>
    </div>
    <div class="coach trainer" style="left:565px;top:58px">
      <div class="photo" role="img" aria-label="Headshot of trainer Carter Bellamy"></div>
      <p class="coach-name">Carter Bellamy</p>
      <p class="coach-role">Former Pro Pitcher Minors<br>(Monarchs, Larks, Riverton</p>
    </div>
    <div class="coach trainer" style="left:889px;top:58px;width:360px">
      <div class="photo" role="img" aria-label="Team photo with trainer Miles Hadley"></div>
      <p class="coach-name">Miles Hadley</p>
      <p class="coach-role large">former Pro Pitcher Minors (Titans)</p>
      <p class="coach-role">Pitching &amp; Hitting Instructor</p>
    </div>
    <div class="coach trainer" style="left:207px;top:343px">
      <div class="photo" role="img" aria-label="Headshot of trainer Rowan Mercer"></div>
      <p class="coach-name">Rowan Mercer</p>
      <p class="coach-role">Hitting Played professionally after<br>College in the Independent<br>Leagueon the West Coach</p>
    </div>
    <div class="coach trainer" style="left:565px;top:343px">
      <div class="photo" role="img" aria-label="Headshot of trainer Kieran Whitlock"></div>
      <p class="coach-name">Kieran Whitlock</p>
      <p class="coach-role">Infield &amp; Hitting Current<br>College Coach;<br>FormerCollege Shortstop</p>
    </div>
    <div class="coach trainer" style="left:889px;top:343px">
      <div class="photo" role="img" aria-label="Photo of trainer Grant Calloway coaching"></div>
      <p class="coach-name">Grant Calloway</p>
      <p class="coach-role">Catching &amp; HittingCurrent HS<br>Coach &amp; 16u Showcase Coach</p>
    </div>
  </section>

  <div class="banner banner-private">Private Instuction</div>

  <section class="lesson-section">
    <svg class="stripes" width="1100" height="559" viewBox="0 0 1100 559" aria-hidden="true">
      <polygon points="0,0 70,0 0,200" fill="#e8141b"/>
      <polygon points="260,0 330,0 60,559 0,559" fill="#e2e3e6" opacity=".7"/>
      <polygon points="760,0 840,0 560,559 480,559" fill="#e2e3e6" opacity=".7"/>
      <polygon points="1100,400 1100,559 1040,559" fill="#e8141b"/>
    </svg>
    <div class="coach lesson" style="left:152px;top:13px">
      <div class="photo" role="img" aria-label="Headshot of coach Aaron Dalby"></div>
      <p class="coach-name">Aaron Dalby</p>
      <p class="coach-role">Hitting &amp; PitchingFormer College<br>Coach &amp; CurrentHigh School</p>
    </div>
    <div class="coach lesson" style="left:416px;top:13px">
      <div class="photo" role="img" aria-label="Headshot of coach Zane Norwood"></div>
      <p class="coach-name">Zane Norwood</p>
      <p class="coach-role">Hitting &amp; Defense Former<br>College Player &amp; former<br>HS Coach</p>
    </div>
    <div class="coach lesson" style="left:681px;top:13px">
      <div class="photo" role="img" aria-label="Headshot of coach Kurt Selwyn"></div>
      <p class="coach-name">Kurt Selwyn</p>
      <p class="coach-role">Hitting &amp; InfieldFormer College<br>&amp; former Pro PlayerCurrent 16u<br>Showcase Coach</p>
    </div>
    <div class="coach lesson" style="left:945px;top:13px">
      <div class="photo" role="img" aria-label="Headshot of coach Jonah Galvez"></div>
      <p class="coach-name">Jonah Galvez</p>
      <p class="coach-role">Catching &amp; HittingCurrent<br>college coach; works<br>Slate Harbor's Camps</p>
    </div>
    <div class="coach lesson" style="left:152px;top:265px">
      <div class="photo" role="img" aria-label="Headshot of coach Reid Stanton"></div>
      <p class="coach-name">Reid Stanton</p>
      <p class="coach-role">Catching &amp; Hitting Current<br>College Coach &amp; former player</p>
    </div>
    <div class="coach lesson" style="left:416px;top:265px">
      <div class="photo" role="img" aria-label="Photo of coach Pierce Kemper on the field"></div>
      <p class="coach-name">Pierce Kemper</p>
      <p class="coach-role">Hitting &amp; Catching Former<br>College Coach &amp; HS Head Coach</p>
    </div>
    <div class="coach lesson" style="left:681px;top:265px">
      <div class="photo" role="img" aria-label="Headshot of coach Marcus Whitlock"></div>
      <p class="coach-name">Marcus Whitlock</p>
      <p class="coach-role">Hitting &amp; Defense<br>Current HS Head Coach and<br>15u Showcase Coach</p>
    </div>
    <div class="coach lesson" style="left:945px;top:265px">
      <div class="photo" role="img" aria-label="Headshot of coach Harjit Sohal"></div>
      <p class="coach-name">Harjit Sohal</p>
      <p class="coach-role">Hitting &amp; Infield Former College<br>Player &amp; Current HS Coach</p>
    </div>
  </section>

  <div class="seam seam-left"></div>
  <div class="seam seam-right"></div>
  <div class="banner banner-lessons">Lessons</div>

  <footer class="footer">
    <span class="rule"></span>
    <span class="url">WWW.<b>SLATEHARBORFIT</b>.EXAMPLE</span>
    <span class="rule"></span>
  </footer>
</main>
</body>
</html>
```